Sign - Pricing "Menu" Board
Pimble Grove
Project: Sign - Pricing "Menu" Board
Sign - Pricing "Menu" Board  - Children
Creative Brief
This sign will be printed and be placed over desk for all customers to view. It will be in very large print in the front entrance for our new business so provide a quick pricing guide for our services. Our website can be viewed at https://pimblegrove.example.
Children
parents with kids under 7, day cares, pre-schools, grandparents, elementary schools
1. Cohesive feel with website 2. Include all of our services - Drop In Play, Pimble Sparks Programs, Memberships, Kids Night Out, Birthday Parties, Socks - $2 a pair Harriet & Gus Toys - prices vary 3. Our play place will feature home build by Tobby Nook homes. You can use photos from there site if you want. The playhouses can be found in their main street collection - we will feature (market, gas station, dr. office, animal hospital, diner) 4. We are looking for fun quick way for customers to see the pricing when they come in. 5. Everyone will need to sign a waiver to play. That should be included some place on the sign.

```html
<!DOCTYPE html>
<html lang="en">
<head>
<meta charset="utf-8">
<title>Pimble Grove – Pricing Menu Board</title>
<link href="https://fonts.googleapis.com/css2?family=Arvo:wght@400;700&family=Open+Sans:wght@400;600;700&display=swap" rel="stylesheet">
<style>
  :root{
    --stage:#e6e7e8;
    --label:#5a5a5a;
    --blue:#1f4f9c;
    --blue-deep:#173f82;
    --blue-title:#1d58a8;
    --green:#72b62a;
    --green-deep:#4f9a1c;
    --green-light:#a6d45a;
    --box-line:#8cc63f;
    --ink:#2a2a2a;
    --muted:#555555;
    --white:#ffffff;
  }
  *{box-sizing:border-box;margin:0;padding:0}
  html,body{width:1200px;height:910px;overflow:hidden}
  body{background:var(--stage);font-family:"Open Sans",Arial,sans-serif;color:var(--ink);position:relative}

  .sheet-label{position:absolute;left:20px;font-size:14px;color:var(--label)}
  .sheet-label--one{top:16px}
  .sheet-label--two{top:447px}

  .sheet{position:absolute;left:86px;width:1034px;overflow:hidden;
    background:linear-gradient(160deg,var(--blue) 0%,var(--blue-deep) 100%);
    box-shadow:0 2px 6px rgba(0,0,0,.25)}
  .sheet--one{top:44px;height:386px}
  .sheet--two{top:475px;height:391px}

  .sheet__photo{position:absolute;left:0;top:0;width:340px;height:150px;
    background:linear-gradient(100deg,#d9c7ae 0%,#eadcc8 45%,#c9d3b8 100%)}
  .sheet__wave{position:absolute;left:0;top:0;width:1034px;height:160px}

  .masthead{position:absolute;left:505px;top:8px;font-family:"Arvo",Georgia,serif;font-weight:700}
  .masthead__welcome{font-size:23px;color:var(--blue-title);line-height:1}
  .masthead__name{font-size:58px;color:var(--green);line-height:1.1;letter-spacing:-.5px}

  .price-box{position:absolute;background:var(--white);border:2px solid var(--box-line);border-radius:6px;overflow:hidden;
    box-shadow:0 1px 3px rgba(0,0,0,.3)}
  .price-box__head{background:linear-gradient(180deg,var(--green-light),var(--green) 55%,var(--green-deep));
    color:var(--white);font-family:"Arvo",Georgia,serif;font-weight:700;text-align:center;font-size:13px;line-height:1.15;padding:5px 6px}
  .price-box__body{padding:6px 8px;font-size:9.5px;line-height:1.3}
  .price-list{list-style:none}
  .price-list li{position:relative;padding-left:15px;margin-bottom:4px}
  .price-list li::before{content:"";position:absolute;left:2px;top:1px;width:5px;height:9px;
    border:solid var(--green-deep);border-width:0 2.5px 2.5px 0;transform:rotate(40deg)}
  .note{font-size:8.5px;line-height:1.3;color:var(--muted);margin:2px 0 5px 15px}
  .strong{font-weight:700}
  .nowrap{white-space:nowrap}

  /* Sheet 1 positions */
  .box-weekdays{left:148px;top:152px;width:160px;height:98px}
  .box-weekends{left:148px;top:258px;width:160px;height:122px}
  .box-night{left:320px;top:152px;width:185px;height:228px}
  .box-drop{left:517px;top:152px;width:183px;height:98px}
  .box-members{left:517px;top:258px;width:183px;height:122px}
  .box-sparks{left:714px;top:152px;width:209px;height:228px}

  /* Sheet 2 positions */
  .box-packages{left:250px;top:146px;width:250px;height:234px}
  .box-includes{left:514px;top:146px;width:262px;height:234px}
  .sheet--two .price-box__head{font-size:16px;padding:7px 10px}
  .sheet--two .price-box__body{font-size:11.5px;padding:10px 12px}
  .sheet--two .price-list li{padding-left:17px;margin-bottom:8px}
  .sheet--two .note{font-size:10.5px;margin:0 0 6px 17px}
</style>
</head>
<body>

<div class="sheet-label sheet-label--one">Sheet 1</div>
<section class="sheet sheet--one">
  <div class="sheet__photo" role="img" aria-label="Photo of a smiling young child at play in the play place"></div>
  <svg class="sheet__wave" viewBox="0 0 1034 160" preserveAspectRatio="none" aria-hidden="true">
    <path d="M330,0 H1034 V118 C800,100 610,118 430,110 C380,108 350,112 330,114 Z" fill="#ffffff"/>
    <path d="M0,140 C200,136 300,108 430,112 C610,120 800,100 1034,118 V134 C800,118 610,138 430,130 C300,126 200,152 0,158 Z" fill="#5ea51f"/>
    <path d="M0,140 C200,136 300,108 430,112 C610,120 800,100 1034,118" fill="none" stroke="#a6d45a" stroke-width="4"/>
  </svg>
  <header class="masthead">
    <div class="masthead__welcome">Welcome to Our</div>
    <div class="masthead__name">Pimble Grove.</div>
  </header>

  <div class="price-box box-weekdays">
    <div class="price-box__head">Weekdays</div>
    <div class="price-box__body"><ul class="price-list">
      <li><span class="strong">Main Floor</span><br>Garden Party ..... $150</li>
      <li><span class="strong">Mezzanine</span><br>Tree Top Party .... $175</li>
    </ul></div>
  </div>

  <div class="price-box box-weekends">
    <div class="price-box__head">Weekends</div>
    <div class="price-box__body"><ul class="price-list">
      <li><span class="strong">Main Floor</span><br>Garden Party ..... $250</li>
      <li><span class="strong">Mezzanine</span><br>Tree Top Party .... $275<br>Busy Bee Package .. $650</li>
    </ul></div>
  </div>

  <div class="price-box box-night">
    <div class="price-box__head">Kids Night Out</div>
    <div class="price-box__body"><ul class="price-list">
      <li class="strong">Every Thursday Night<br>From 5pm – 9pm</li>
      <li><span class="strong">$25</span> per child<br><span class="strong">$20</span> each additional sibling</li>
    </ul>
    <p class="note">Must reserve spot, limited availability</p>
    <ul class="price-list"><li class="strong">Everyone is required to sign a waiver</li></ul>
    <p class="note">Children must be supervised at all times</p>
    </div>
  </div>

  <div class="price-box box-drop">
    <div class="price-box__head">Drop In Play</div>
    <div class="price-box__body"><ul class="price-list">
      <li>General Admission .. $12</li>
      <li>Each additional sibling .. $10</li>
    </ul></div>
  </div>

  <div class="price-box box-members">
    <div class="price-box__head">Monthly<br>Memberships</div>
    <div class="price-box__body"><ul class="price-list">
      <li><span class="strong">$45</span> Single</li>
      <li><span class="strong">$80</span> Family</li>
      <li>Socks are Required<br><span class="strong">$2.00</span> a pair</li>
    </ul></div>
  </div>

  <div class="price-box box-sparks">
    <div class="price-box__head">Pimble Sparks<br>Programs</div>
    <div class="price-box__body"><ul class="price-list">
      <li><span class="strong">Tuesday</span><br>Craft Activity ......... $3.00</li>
      <li><span class="strong">Wednesday</span><br>STEM Activity ......... $3.00</li>
      <li><span class="strong">Thursday</span><br>Interactive Reading Activity .. $3.00</li>
      <li><span class="strong">Friday</span><br>Music Activity ......... $3.00</li>
    </ul>
    <p class="note">(Plus cost of General Admission)</p>
    </div>
  </div>
</section>

<div class="sheet-label sheet-label--two">Sheet 2</div>
<section class="sheet sheet--two">
  <div class="sheet__photo" role="img" aria-label="Photo of a smiling young child at play in the play place"></div>
  <svg class="sheet__wave" viewBox="0 0 1034 160" preserveAspectRatio="none" aria-hidden="true">
    <path d="M330,0 H1034 V118 C800,100 610,118 430,110 C380,108 350,112 330,114 Z" fill="#ffffff"/>
    <path d="M0,140 C200,136 300,108 430,112 C610,120 800,100 1034,118 V134 C800,118 610,138 430,130 C300,126 200,152 0,158 Z" fill="#5ea51f"/>
    <path d="M0,140 C200,136 300,108 430,112 C610,120 800,100 1034,118" fill="none" stroke="#a6d45a" stroke-width="4"/>
  </svg>
  <header class="masthead">
    <div class="masthead__welcome">Welcome to Our</div>
    <div class="masthead__name">Pimble Grove.</div>
  </header>

  <div class="price-box box-packages">
    <div class="price-box__head">We offer three<br>party packages</div>
    <div class="price-box__body"><ul class="price-list">
      <li><span class="strong">Main Floor Garden Party</span><br><span class="nowrap">$150 Weekdays | $250 Weekends</span></li>
      <li><span class="strong">Mezzanine Tree Top Party</span><br><span class="nowrap">$175 Weekdays | $275 Weekends</span></li>
      <li><span class="strong">Busy Bee Party</span><br>$650 Any Day</li>
    </ul></div>
  </div>

  <div class="price-box box-includes">
    <div class="price-box__head">All party<br>packages include</div>
    <div class="price-box__body"><ul class="price-list">
      <li class="strong">Two hours of play time</li>
      <li class="strong">Pimble Grove party invitations</li>
      <li><span class="strong">Tableware</span> plates and utensils, favor-size drinks</li>
    </ul>
    <p class="note">Water and organic juice for each party guest</p>
    <p class="note">Up to 15 children in the main floor / up to 25 children in mezzanine</p>
    </div>
  </div>
</section>

</body>
</html>
```